Holvik Cabinets Quality Custom Built Kitchens, Vanity Units, Robes ect

Hi,
Was after a new design for our business cards,
we are a cabinet making business and pride ourselves in quality custom built Kitchens, Vanity units, robes ect.
we have been around for over 20 years and we are trying to modernize our card logo.
Looking for something eye catching, bold and exciting
family ran and operated business, we work with builders and also have a large private clientel.

Thanks

Industry/Entity Type

Business

Contact Information for Business Card

Holvik Cabinets

Font styles to use
Serif
Script

Requirements
Must have
• Corinne 0461735928 hvcabinets@mailvane.com
• Po Box 2786
• 5B Wattlebark Court Brennock Vic 3871
• Phone (03)59286417 Fax (03) 59286942
Nice to have
• Quality Custom Built Kitchens & Vanity Units

```html
<!DOCTYPE html>
<html lang="en">
<head>
<meta charset="utf-8">
<title>Holvik Cabinets – Business Card</title>
<link rel="stylesheet" href="https://fonts.googleapis.com/css2?family=Montserrat:wght@600&family=Arimo:wght@400;700&display=swap">
<style>
  :root {
    --backdrop: #8b8a74;
    --card: #eceae3;
    --ink-navy: #1d3a4f;
    --ink-text: #1e1e1e;
    --rule: #4a4a4a;
  }
  * { box-sizing: border-box; margin: 0; padding: 0; }
  html, body {
    width: 1200px;
    height: 800px;
    overflow: hidden;
    background: var(--backdrop);
  }
  .canvas {
    position: relative;
    width: 1200px;
    height: 800px;
  }
  .business-card {
    position: absolute;
    left: 100px;
    top: 95px;
    width: 1000px;
    height: 611px;
    background: var(--card);
    box-shadow: 0 10px 30px rgba(0, 0, 0, 0.25);
  }
  .wordmark {
    position: absolute;
    left: 128px;
    top: 88px;
    font-family: "Montserrat", sans-serif;
    font-weight: 600;
    font-size: 60px;
    line-height: 1;
    letter-spacing: 1px;
    color: var(--ink-navy);
    text-transform: uppercase;
    white-space: nowrap;
  }
  .contact-table {
    position: absolute;
    left: 125px;
    top: 210px;
    width: 755px;
    border: 1.5px solid var(--rule);
    font-family: "Arimo", sans-serif;
    color: var(--ink-text);
  }
  .contact-row {
    display: flex;
    height: 68px;
    border-top: 1.5px solid var(--rule);
  }
  .contact-row:first-child { border-top: none; }
  .contact-cell {
    display: flex;
    align-items: center;
    padding: 0 24px;
    font-size: 24px;
    white-space: nowrap;
  }
  .contact-cell + .contact-cell { border-left: 1.5px solid var(--rule); }
  .person-name {
    flex: 1;
    justify-content: center;
    font-weight: 700;
    font-size: 32px;
    letter-spacing: 0.5px;
    text-transform: uppercase;
  }
  .mobile { width: 250px; }
  .email { flex: 1; justify-content: center; }
  .street-address { width: 535px; }
  .po-box { flex: 1; justify-content: center; }
  .phone { width: 275px; }
  .fax { flex: 1; }
</style>
</head>
<body>
  <div class="canvas">
    <section class="business-card" aria-label="Holvik Cabinets business card">
      <h1 class="wordmark">Holvik Cabinets</h1>
      <div class="contact-table">
        <div class="contact-row">
          <div class="contact-cell person-name">Corinne</div>
        </div>
        <div class="contact-row">
          <div class="contact-cell mobile">0461735928</div>
          <div class="contact-cell email">E: hvcabinets@mailvane.com</div>
        </div>
        <div class="contact-row">
          <div class="contact-cell street-address">5B Wattlebark Court Brennock Vic 3871</div>
          <div class="contact-cell po-box">Po Box 2786</div>
        </div>
        <div class="contact-row">
          <div class="contact-cell phone">P: (03)59286417</div>
          <div class="contact-cell fax">F: (03) 59286942</div>
        </div>
      </div>
    </section>
  </div>
</body>
</html>
```